B7r Website Design

We need a website design, look, feel and functionality that uses a recently approved logo attached. This should be a highly professional looking website that is relatively simple, but scalable. The website should carry information about the company, links and blog posts. The look and feel of the website should be consistent with the logo colour palette, but does not have to stick to them exactly. The company provides high quality brokering and support services for multinational companies to work with international humanitarian organisations and the Allied Concord. Where possible, the design should make the most of the concept that collective action has a greater impact, and that Coalition9Reach can help make that happen. The attached text can be used as a basis for the website text.

Target Market(s)

Heads of company foundations, and humanitarian organisations, and Allied Concord departments the promote collaboration

Number of Pages Required

3 page

Requirements
Should not have
• Photos of people in suits.
• Photos of poor African children begging for help, or smiling in gratitude for aid

```html
<!DOCTYPE html>
<html lang="en">
<head>
<meta charset="utf-8">
<title>Coalition9Reach</title>
<link rel="stylesheet" href="https://fonts.googleapis.com/css2?family=Montserrat:wght@400;500;600;700&display=swap">
<style>
:root{
  --blue:#3a44a0;
  --orange:#f0592a;
  --ink:#1d1d22;
  --text:#333338;
  --white:#ffffff;
  --footer:#2a2a2e;
  --line:#3a44a0;
}
*{box-sizing:border-box;margin:0;padding:0}
html,body{width:727px;height:1200px;overflow:hidden;background:var(--white)}
body{position:relative;font-family:"Montserrat",sans-serif;color:var(--text)}
.abs{position:absolute}
.nav a{position:absolute;top:26px;font-size:8.5px;color:var(--text);text-decoration:none}
.brand{position:absolute;left:0;width:727px;top:18px;text-align:center;font-size:19px;font-weight:600;color:var(--blue);letter-spacing:-0.2px}
.hero{position:absolute;left:0;top:66px;width:727px;height:343px;background:linear-gradient(135deg,#4a3a2e 0%,#6d5a4a 35%,#8a8584 60%,#3f3b3a 100%)}
.hero::after{content:"";position:absolute;inset:0;background:rgba(20,20,25,.35)}
.hero-copy{position:absolute;left:0;top:96px;width:727px;text-align:center;color:var(--white);z-index:1}
.hero-copy h1{font-size:28px;font-weight:600;line-height:33px}
.hero-copy p{font-size:13.5px;line-height:16px;margin-top:11px;font-weight:500}
.btn-discover{position:absolute;left:326px;top:331px;width:74px;height:21px;border-radius:11px;background:var(--orange);color:var(--white);font-size:8.5px;font-weight:500;text-align:center;line-height:21px;z-index:1}
.about-photo{position:absolute;left:406px;top:409px;width:321px;height:191px;background:linear-gradient(90deg,#ffffff 0%,#8e9ad8 18%,#5860b8 45%,#7a6a4a 75%,#c9a050 100%)}
.about h2{position:absolute;left:117px;top:439px;font-size:11px;font-weight:600;color:var(--blue)}
.about p{position:absolute;left:117px;top:460px;width:225px;font-size:8.3px;line-height:13.8px;text-align:justify;color:var(--text)}
.btn-read{position:absolute;left:117px;top:566px;width:74px;height:21px;border-radius:11px;background:var(--blue);color:var(--white);font-size:7.5px;font-weight:500;text-align:center;line-height:21px}
.pillar-title{position:absolute;font-size:11px;font-weight:600;color:var(--blue);text-align:center;width:120px}
.pillar-text{position:absolute;font-size:8.2px;font-weight:600;line-height:10.3px;color:var(--ink)}
.tree{position:absolute;background:var(--line)}
.value{position:absolute;top:842px;width:96px;text-align:center}
.value svg{display:block;margin:0 auto}
.value p{margin-top:5px;font-size:8.2px;line-height:10.2px;color:var(--ink)}
.contact{position:absolute;left:0;top:967px;width:727px;height:200px;background:var(--blue);color:var(--white)}
.contact h2{position:absolute;left:334px;top:24px;font-size:10.5px;font-weight:600}
.info{position:absolute;left:156px;font-size:7.8px;line-height:9.6px}
.info b{font-weight:600;display:block}
.field{position:absolute;background:var(--white);border-radius:2px;color:#8a8a90;font-size:7.5px;padding:5px 6px}
.footer{position:absolute;left:0;top:1167px;width:727px;height:33px;background:var(--footer);color:var(--white);font-size:7px}
.footer span{position:absolute;top:12px}
</style>
</head>
<body>
<nav class="nav">
  <a style="left:133px">Home</a>
  <a style="left:171px">About</a>
  <a style="left:210px">Vision</a>
  <a style="left:469px">News</a>
  <a style="left:507px">Blog</a>
  <a style="left:545px">Contact us</a>
</nav>
<div class="brand">Coalition9Reach</div>

<section class="hero" role="img" aria-label="Photo of two hands shaking over a desk with papers and a laptop"></section>
<div class="hero-copy" style="top:162px">
  <h1>Facilitating cross sector<br>collaboration for social good</h1>
  <p>A service that advocates, unites and supports<br>collaborative resilience to humanitarian crises</p>
</div>
<div class="btn-discover">Discover</div>

<section class="about">
  <h2>About us</h2>
  <p>Based in Geneva, Switzerland – renowned as the world’s humanitarian capital – B7r facilitates cross sector collaboration for social good. It was founded in response to the growing need for independent quality support for collaboration between different sectors of society attempting to achieve practical objectives of mutual interest.</p>
  <div class="btn-read">Read more</div>
</section>
<div class="about-photo" role="img" aria-label="Evening view of the Geneva lakefront with the water fountain"></div>

<!-- Vision -->
<svg class="abs" style="left:167px;top:662px" width="30" height="20" viewBox="0 0 30 20"><path d="M1 10 Q15 -4 29 10 Q15 24 1 10Z" fill="none" stroke="#111" stroke-width="1.6"/><circle cx="15" cy="10" r="5.5" fill="none" stroke="#111" stroke-width="1.6"/><circle cx="15" cy="10" r="3.2" fill="#111"/></svg>
<div class="pillar-title" style="left:122px;top:694px">Vision</div>
<div class="pillar-text" style="left:124px;top:716px;width:115px">A world in which people have greater control over their resilience to potential humanitarian crises</div>

<!-- Values -->
<svg class="abs" style="left:348px;top:677px" width="32" height="32" viewBox="0 0 32 32" fill="none" stroke="#111" stroke-width="1.4"><path d="M4 12 L6 24 L12 30 M28 12 L26 24 L20 30"/><path d="M8 16 L12 22 L15 23 M24 16 L20 22 L17 23"/><path d="M16 2v5M13.5 4.5h5M11 10v3M9.5 11.5h3M21 10v3M19.5 11.5h3M16 13v4M14 15h4"/></svg>
<div class="pillar-title" style="left:304px;top:714px">Values</div>

<!-- Mission -->
<svg class="abs" style="left:536px;top:653px" width="34" height="36" viewBox="0 0 34 36" fill="none" stroke="#111" stroke-width="1.3"><circle cx="7" cy="7" r="3"/><path d="M7 1v2M7 11v2M1 7h2M11 7h2M2.8 2.8l1.4 1.4M9.8 9.8l1.4 1.4M2.8 11.2l1.4-1.4M9.8 4.2l1.4-1.4"/><path d="M2 34 L13 20 L18 26 L22 21 L32 34Z"/><path d="M22 21V9h6v4h-6"/></svg>
<div class="pillar-title" style="left:492px;top:694px">Mission</div>
<div class="pillar-text" style="left:495px;top:716px;width:116px;text-align:justify">B7r commitment to that vision is to increase effective collaboration between different sectors of society on resilience building objectives of mutual benefit</div>

<!-- tree -->
<div class="tree" style="left:363px;top:735px;width:1.5px;height:70px"></div>
<div class="tree" style="left:156px;top:804px;width:418px;height:1.5px"></div>
<div class="tree" style="left:155px;top:804px;width:1.5px;height:18px"></div>
<div class="tree" style="left:258px;top:804px;width:1.5px;height:18px"></div>
<div class="tree" style="left:363px;top:804px;width:1.5px;height:18px"></div>
<div class="tree" style="left:467px;top:804px;width:1.5px;height:18px"></div>
<div class="tree" style="left:572px;top:804px;width:1.5px;height:18px"></div>

<div class="value" style="left:105px">
  <svg width="40" height="28" viewBox="0 0 40 28" fill="none" stroke="#111" stroke-width="1.4"><path d="M2 8 L8 3 L14 6 L20 5 L28 3 L38 9 L34 14 L24 24 L18 26 L8 18 L3 12Z"/><path d="M14 6 L10 12 L14 14 L20 9 L28 16"/><path d="M12 18l4 4M16 15l5 5M20 13l5 5"/></svg>
  <p>Cross sector partnerships are between equals</p>
</div>
<div class="value" style="left:210px">
  <svg width="28" height="28" viewBox="0 0 28 28" fill="none" stroke="#111" stroke-width="1.3"><circle cx="9" cy="3" r="2"/><circle cx="14" cy="3" r="2"/><circle cx="19" cy="3" r="2"/><circle cx="5" cy="9" r="2"/><circle cx="23" cy="9" r="2"/><path d="M2 22V14q3-3 6 0v13M26 22V14q-3-3-6 0v13M9 27V12q5-4 10 0v15M14 14v13"/></svg>
  <p>Self-sufficient societies are more effective societies</p>
</div>
<div class="value" style="left:316px">
  <svg width="36" height="30" viewBox="0 0 36 30" fill="none" stroke="#111" stroke-width="1.3"><circle cx="18" cy="4" r="3"/><path d="M12 14q6-7 12 0"/><circle cx="9" cy="18" r="2.6"/><circle cx="27" cy="18" r="2.6"/><circle cx="18" cy="18" r="2.6"/><path d="M3 29q6-7 12 0M12 29q6-7 12 0M21 29q6-7 12 0"/><path d="M5 10q2-4 6-5M31 10q-2-4-6-5"/></svg>
  <p>Collaborative action is an investment in a joint objective</p>
</div>
<div class="value" style="left:420px">
  <svg width="30" height="28" viewBox="0 0 30 28"><path d="M15 26 L3 14 Q-1 7 5 3 Q11 0 15 6 Q19 0 25 3 Q31 7 27 14Z" fill="none" stroke="#111" stroke-width="2.2"/></svg>
  <p>Humility is the most effective methodology</p>
</div>
<div class="value" style="left:525px">
  <svg width="30" height="32" viewBox="0 0 30 32" fill="none" stroke="#111" stroke-width="1.4"><circle cx="15" cy="4" r="2"/><circle cx="4" cy="11" r="2"/><circle cx="26" cy="11" r="2"/><circle cx="7" cy="25" r="2"/><circle cx="23" cy="25" r="2"/><path d="M15 7v5M11 9l4 3 4-3M6 14l4 3M24 14l-4 3M9 22l3-4M21 22l-3-4M12 29l3-3 3 3"/></svg>
  <p>humanitarian principles must be shared and encouraged</p>
</div>

<section class="contact">
  <h2>Contact us</h2>
  <div class="info" style="top:45px"><b>Email</b>contact@coalition9reach.com</div>
  <div class="info" style="top:74px"><b>Phone numbers</b>202-555-0147<br>202-555-0183</div>
  <div class="info" style="top:112px"><b>Address</b>Coalition9Reach<br>Lakeview Hall SA<br>P.O Box 348<br>1209 Rivemont / Geneva</div>
  <div class="field" style="left:334px;top:49px;width:110px;height:19px">Name</div>
  <div class="field" style="left:448px;top:49px;width:122px;height:19px">Email</div>
  <div class="field" style="left:334px;top:71px;width:236px;height:19px">Inquiry Type
    <svg class="abs" style="right:8px;top:7px" width="9" height="6" viewBox="0 0 9 6"><path d="M1 1l3.5 3.5L8 1" fill="none" stroke="#222" stroke-width="1.5"/></svg>
  </div>
  <div class="field" style="left:334px;top:95px;width:236px;height:76px">Message...</div>
</section>

<footer class="footer">
  <span style="left:117px">Coalition9Reach © 2018</span>
  <span style="left:466px">Terms of Service | Privacy Policy | Cookies</span>
</footer>
</body>
</html>
```